integrative health clinic-Medical massage, acupuncture, chiropractic

we like our logo, but are open to new ideas. We need a new card design. We have added chiropractic and acupuncture that we have put under the name of the business. We are an integrative medical clinic

Target Market(s)

General public, athletes

Contact Information for Business Card

Phone 5055583927
Fax 5055583926
Hours Monday-Friday 9-6
Saturday 10-6
The 20% can be smaller on the back

Colors
3176b5
0355a3

Requirements
Must have
• Logo but am open to ideas
Nice to have
• We are an integrated medical clinic but also want to be personable. We want the card fun and inviting

```html
<!DOCTYPE html>
<html lang="en">
<head>
<meta charset="utf-8">
<title>Clear Path Wellness – Business Card</title>
<link href="https://fonts.googleapis.com/css2?family=Roboto+Condensed:wght@400;700&family=Roboto:wght@400&family=Crimson+Text:wght@400&display=swap" rel="stylesheet">
<style>
  :root{
    --stage:#2b2b2b;
    --blue-deep:#0355a3;
    --blue-light:#3176b5;
    --ink:#1c1c1c;
    --white:#ffffff;
  }
  *{margin:0;padding:0;box-sizing:border-box}
  html,body{width:1200px;height:901px;overflow:hidden;background:var(--stage)}
  .canvas{position:relative;width:1200px;height:901px}
  .card{position:absolute;left:250px;width:700px;height:400px;overflow:hidden}

  /* back */
  .card-back{top:35px;background:linear-gradient(135deg,var(--blue-deep) 0%,var(--blue-deep) 55%,var(--blue-light) 100%);color:var(--white)}
  .card-back .brand{position:absolute;top:120px;left:0;width:100%;text-align:center}
  .brand-name{font-family:"Roboto Condensed",sans-serif;font-weight:400;font-size:50px;letter-spacing:-0.5px;line-height:1}
  .brand-tagline{font-family:"Crimson Text",serif;font-size:22px;margin-top:8px;letter-spacing:.5px}
  .hours{position:absolute;left:0;bottom:38px;width:100%;text-align:center;font-family:"Roboto",sans-serif;font-size:14px;letter-spacing:1px}
  .hours-title{display:flex;align-items:center;justify-content:center;gap:8px;font-size:13px;margin-bottom:4px}
  .hours-title::before,.hours-title::after{content:"";width:90px;height:1px;background:var(--white);opacity:.8}

  /* front */
  .card-front{top:465px;background:var(--white)}
  .card-front .swoosh{position:absolute;inset:0}
  .card-front .brand{position:absolute;top:40px;left:50px;color:var(--ink)}
  .card-front .brand-tagline{color:var(--blue-deep);margin-left:4px}
  .person{position:absolute;left:50px;top:215px}
  .person-name{font-family:"Roboto Condensed",sans-serif;font-weight:700;font-size:32px;color:var(--blue-deep);line-height:1}
  .person-role{font-family:"Roboto Condensed",sans-serif;font-size:16px;color:var(--ink);margin-top:4px}
  .contacts{position:absolute;left:360px;top:255px;list-style:none;font-family:"Roboto",sans-serif;font-size:17px;letter-spacing:1.6px;color:var(--ink)}
  .contacts li{display:flex;align-items:center;gap:12px;height:31px}
  .contacts svg{width:18px;height:18px;flex:none;fill:var(--blue-deep)}
</style>
</head>
<body>
<main class="canvas">

  <section class="card card-back" aria-label="Card back">
    <div class="brand">
      <div class="brand-name">Clear Path Wellness</div>
      <div class="brand-tagline">Sports Therapy and Wellness Center</div>
    </div>
    <div class="hours">
      <div class="hours-title">Hours Of Operation</div>
      <div class="hours-times">Friday&nbsp; 9 am - 6 pm &nbsp;|&nbsp; Saturday&nbsp; 10 am - 6 pm</div>
    </div>
  </section>

  <section class="card card-front" aria-label="Card front">
    <svg class="swoosh" viewBox="0 0 700 400" preserveAspectRatio="none" aria-hidden="true">
      <defs>
        <linearGradient id="swooshFill" x1="0" y1="0" x2="1" y2="1">
          <stop offset="0" stop-color="#0355a3"/>
          <stop offset=".5" stop-color="#3176b5"/>
          <stop offset="1" stop-color="#0355a3"/>
        </linearGradient>
      </defs>
      <path d="M280,0 H700 V345 C630,175 470,55 280,0 Z" fill="#3176b5"/>
      <path d="M335,0 H700 V300 C630,160 490,50 335,0 Z" fill="url(#swooshFill)"/>
      <path d="M318,0 C480,50 630,165 700,318" fill="none" stroke="#ffffff" stroke-width="2.5"/>
    </svg>

    <div class="brand">
      <div class="brand-name">Clear Path Wellness</div>
      <div class="brand-tagline">Sports Therapy and Wellness Center</div>
    </div>

    <div class="person">
      <div class="person-name">Sure Name</div>
      <div class="person-role">CEO/Owner</div>
    </div>

    <ul class="contacts">
      <li>
        <svg viewBox="0 0 18 18"><path d="M5 1h8a1.5 1.5 0 0 1 1.5 1.5v13A1.5 1.5 0 0 1 13 17H5a1.5 1.5 0 0 1-1.5-1.5v-13A1.5 1.5 0 0 1 5 1zm0 2.5v10h8v-10z"/></svg>
        505-558-3927
      </li>
      <li>
        <svg viewBox="0 0 18 18"><path d="M1 6c0-2 3-3.5 8-3.5S17 4 17 6v1.5h-3.5V6h-9v1.5H1z"/><path d="M3.5 9h11l1 7h-13z"/></svg>
        505-558-3926
      </li>
      <li>
        <svg viewBox="0 0 18 18"><path d="M1 4h16v10H1zm1.5 1.3v.3L9 10l6.5-4.4v-.3z"/></svg>
        info@clearpathwellnessnm.com
      </li>
      <li>
        <svg viewBox="0 0 18 18"><circle cx="9" cy="9" r="8"/><path d="M9 1v16M1 9h16" stroke="#fff" stroke-width="1.2" fill="none"/></svg>
        www.clearpathwellnessnm.com
      </li>
    </ul>
  </section>

</main>
</body>
</html>
```